DL SIZED ONE SIDED BROCHURE FOR CLEANING AND GARDENING SERVICE

business name: K&T property services
services provided: Strata cleaning,lawn mowing,hedge trimming,garden maintainance,lawn repair,weed spraying/removal, rubbish removal.
10 years experience and fully insured.
obligation free quotes.
phone number:contact doug 0427391054
email: ktpropertyservices@mailvane.example
slogan: when quality matters ring K&T
K&T logo would be nice but not essential
DL size in inches: 3.9in × 8.2in
DL size in millimetres: 100mm × 210mm
DL size in centimetres: 10cm x 21cm
Updates
doing good guys no suggestions except being original
Target Market(s)
real estate agents, private home owners, contractors.
Industry/Entity Type
Business
Look and feel
Each slider illustrates characteristics of the customer's brand and the style your logo design should communicate.

```html
<!DOCTYPE html>
<html lang="en">
<head>
<meta charset="utf-8">
<title>K&amp;T Property Services – DL Brochure</title>
<link rel="stylesheet" href="https://fonts.googleapis.com/css2?family=Mulish:ital,wght@0,300;0,400;1,300;1,400&display=swap">
<style>
  :root {
    --brand-blue: #2446c0;
    --band-blue: #b7c3ec;
    --mist: #eef0fb;
    --soft-text: #bcc6ee;
    --white: #ffffff;
  }
  html, body {
    margin: 0;
    padding: 0;
    overflow: hidden;
    background: var(--white);
  }
  .brochure {
    position: relative;
    width: 1200px;
    height: 2522px;
    overflow: hidden;
    background: var(--white);
    font-family: "Mulish", "Avenir", sans-serif;
  }
  .wave {
    position: absolute;
    inset: 0;
    width: 1200px;
    height: 2522px;
  }
  .brand-mark {
    position: absolute;
    left: 570px;
    top: 80px;
    width: 340px;
    height: 340px;
    background: var(--mist);
  }
  .brand-name {
    position: absolute;
    left: 68px;
    top: 30px;
    margin: 0;
    color: var(--brand-blue);
    font-weight: 300;
    font-size: 190px;
    line-height: 1;
  }
  .brand-name .line {
    display: block;
  }
  .brand-name .line--small {
    font-size: 96px;
    letter-spacing: 7px;
    line-height: 122px;
    margin-left: 4px;
  }
  .service-list {
    position: absolute;
    left: 54px;
    top: 555px;
    margin: 0;
    padding: 0;
    list-style: none;
    color: var(--brand-blue);
    font-style: italic;
    font-weight: 400;
    font-size: 70px;
    line-height: 92px;
  }
  .slogan {
    position: absolute;
    right: 40px;
    top: 1535px;
    margin: 0;
    text-align: right;
    color: var(--white);
    font-weight: 300;
    font-size: 97px;
    line-height: 124px;
  }
  .credentials {
    position: absolute;
    right: 40px;
    top: 1885px;
    margin: 0;
    padding: 0;
    list-style: none;
    text-align: right;
    color: var(--soft-text);
    font-style: italic;
    font-weight: 300;
    font-size: 70px;
    line-height: 92px;
  }
  .contact {
    position: absolute;
    right: 40px;
    top: 2300px;
    margin: 0;
    text-align: right;
    color: var(--white);
    font-style: normal;
    font-weight: 400;
    font-size: 58px;
    line-height: 84px;
  }
  .contact span { display: block; }
</style>
</head>
<body>
<main class="brochure">
  <svg class="wave" viewBox="0 0 1200 2522" aria-hidden="true">
    <path fill="var(--band-blue)" d="M1200 500 C1170 900 1000 1080 780 1210 C520 1360 330 1480 200 1700 C100 1880 40 2050 0 2150 L0 2522 L1200 2522 Z"/>
    <path fill="var(--brand-blue)" d="M1200 620 C1180 950 1030 1130 830 1250 C580 1400 400 1520 270 1740 C160 1930 80 2100 0 2270 L0 2522 L1200 2522 Z"/>
  </svg>

  <div class="brand-mark" aria-hidden="true"></div>
  <h1 class="brand-name">
    <span class="line">K&amp;T</span>
    <span class="line line--small">Property</span>
    <span class="line line--small">Services</span>
  </h1>

  <ul class="service-list">
    <li>Strata cleaning</li>
    <li>Lawn mowing</li>
    <li>Hedge trimming</li>
    <li>Garden maintainance</li>
    <li>Lawn repair</li>
    <li>Weed spraying/removal</li>
    <li>Rubbish removal</li>
  </ul>

  <p class="slogan">When quality<br>matters ring K&amp;T</p>

  <ul class="credentials">
    <li>10 years experience</li>
    <li>fully insured</li>
    <li>obligation free quotes</li>
  </ul>

  <address class="contact">
    <span>Contact Doug: 0427391054</span>
    <span>ktpropertyservices@mailvane.example</span>
  </address>
</main>
</body>
</html>
```